Bref créative
Quorvant Systems
Professional
Ramesh Tolanimurthy
Chief Executive Officer
27 Sec. 61, Kusum Marg
Bhavanipur, Jaipur
RJ 304417 INDIA
ramesh@quorvant.example
www.quorvant.example
Need business cards and stationery. I am open to design ideas and feedback will be provided timely
Our email address for letterhead/fax is contact@quorvant.example. This should be used in all locations except the business card.
Stationary and envelopes with a watermark would look great !
Use Horizontal Logo provided in files.
www.quorvant.example can also be added few lines below the logo

```html
<!DOCTYPE html>
<html lang="en">
<head>
<meta charset="utf-8">
<title>Quorvant Systems – Business Cards</title>
<link rel="stylesheet" href="https://fonts.googleapis.com/css2?family=Noto+Serif:ital,wght@1,400;1,700&family=Open+Sans:wght@400;600;700&display=swap">
<style>
  :root {
    --page-bg: #e9ecef;
    --card-white: #ffffff;
    --blue-deep: #0f62ad;
    --blue-mid: #2a86d1;
    --blue-light: #5fb2ec;
    --text-on-blue: #ffffff;
    --brand-blue: #1a78c8;
    --mark-grey: #b9c0c7;
    --divider: #d6dde3;
  }
  * { margin: 0; padding: 0; box-sizing: border-box; }
  html, body { width: 1200px; height: 852px; overflow: hidden; }
  body { background: var(--page-bg); position: relative; font-family: "Open Sans", sans-serif; }

  .card {
    position: absolute; width: 560px; height: 320px;
    border-radius: 22px; overflow: hidden; display: flex;
    background: var(--card-white);
    box-shadow: 0 10px 26px rgba(0,0,0,.18);
  }
  .card--front { left: 90px; top: 110px; }
  .card--reverse { left: 550px; top: 430px; }

  .info-panel {
    width: 270px; height: 100%; color: var(--text-on-blue);
    background: radial-gradient(ellipse at 50% 55%, var(--blue-light) 0%, var(--blue-mid) 45%, var(--blue-deep) 100%);
    padding: 26px 24px; display: flex; flex-direction: column;
    border-right: 3px solid var(--divider);
  }
  .card--reverse .info-panel { order: 2; border-right: 0; border-left: 3px solid var(--divider); text-align: right; }

  .holder-name { font-family: "Noto Serif", serif; font-style: italic; font-weight: 700; font-size: 19px; line-height: 1.2; }
  .holder-title { font-family: "Noto Serif", serif; font-style: italic; font-size: 12px; margin-top: 2px; }
  .address { font-size: 11.5px; line-height: 1.45; margin-top: 46px; }
  .contacts { list-style: none; margin-top: 18px; font-size: 11.5px; line-height: 1.65; }
  .contacts li { display: flex; align-items: center; gap: 9px; }
  .card--reverse .contacts li { flex-direction: row-reverse; }
  .contacts svg { width: 12px; height: 12px; flex: none; fill: none; stroke: var(--text-on-blue); stroke-width: 1.6; }

  .brand-panel { flex: 1; display: flex; flex-direction: column; align-items: center; justify-content: center; gap: 14px; }
  .brand-dot { width: 96px; height: 96px; border-radius: 50%; background: var(--mark-grey); }
  .brand-name { font-weight: 700; font-size: 24px; color: var(--brand-blue); letter-spacing: .5px; }
</style>
</head>
<body>

<svg width="0" height="0" style="position:absolute">
  <defs>
    <symbol id="ico-phone" viewBox="0 0 12 12"><path d="M3 1 L5 3.5 L4 5 Q5.5 7.5 7 8 L8.5 7 L11 9 L9.5 11 Q4 10 1 2.5 Z"/></symbol>
    <symbol id="ico-mobile" viewBox="0 0 12 12"><rect x="3" y="1" width="6" height="10" rx="1"/><line x1="5" y1="9" x2="7" y2="9"/></symbol>
    <symbol id="ico-fax" viewBox="0 0 12 12"><rect x="1.5" y="5" width="9" height="5" rx="1"/><rect x="3.5" y="1.5" width="5" height="3.5"/></symbol>
    <symbol id="ico-mail" viewBox="0 0 12 12"><rect x="1" y="2.5" width="10" height="7"/><path d="M1 2.5 L6 6.5 L11 2.5"/></symbol>
    <symbol id="ico-web" viewBox="0 0 12 12"><circle cx="6" cy="6" r="5"/><path d="M1 6 H11 M6 1 Q3 6 6 11 Q9 6 6 1"/></symbol>
  </defs>
</svg>

<article class="card card--front">
  <section class="info-panel">
    <h1 class="holder-name">Ramesh Tolanimurthy</h1>
    <p class="holder-title">Chief Executive Officer</p>
    <p class="address">27 Sec. 61, Kusum Marg<br>Bhavanipur, Jaipur<br>RJ 304417 INDIA</p>
    <ul class="contacts">
      <li><svg><use href="#ico-phone"/></svg>91 141 5550142</li>
      <li><svg><use href="#ico-mobile"/></svg>91 9000012345</li>
      <li><svg><use href="#ico-fax"/></svg>91 141 5550142</li>
      <li><svg><use href="#ico-mail"/></svg>ramesh@quorvant.example</li>
      <li><svg><use href="#ico-web"/></svg>www.quorvant.example</li>
    </ul>
  </section>
  <section class="brand-panel">
    <span class="brand-dot"></span>
    <span class="brand-name">Quorvant Systems</span>
  </section>
</article>

<article class="card card--reverse">
  <section class="info-panel">
    <h1 class="holder-name">Ramesh Tolanimurthy</h1>
    <p class="holder-title">Chief Executive Officer</p>
    <p class="address">27 Sec. 61, Kusum Marg<br>Bhavanipur, Jaipur<br>RJ 304417 INDIA</p>
    <ul class="contacts">
      <li><svg><use href="#ico-phone"/></svg>91 141 5550142</li>
      <li><svg><use href="#ico-mobile"/></svg>91 9000012345</li>
      <li><svg><use href="#ico-fax"/></svg>91 141 5550142</li>
      <li><svg><use href="#ico-mail"/></svg>ramesh@quorvant.example</li>
      <li><svg><use href="#ico-web"/></svg>www.quorvant.example</li>
    </ul>
  </section>
  <section class="brand-panel">
    <span class="brand-dot"></span>
    <span class="brand-name">Quorvant Systems</span>
  </section>
</article>

</body>
</html>
```